Business Card for a Wedding Films Business

We require a business card design for our business 'Lewis Marrow Wedding Films'. The logo needs to look classy and high end.

Target Market(s)

Wedding Couples

Contact Information for Business Card

Lewis Marrow Wedding Films
07312 605 227
films@lewismarrowreels.com
www.lewismarrowreels.com

Facebook: @lewismarrowweddingfilms
Instagram: @lewismarrowfilms

Font styles to use
Sans Serif

Requirements
Must have
• Social media icons - Facebook and Instagram

```html
<!DOCTYPE html>
<html lang="en">
<head>
<meta charset="utf-8">
<title>Lewis Marrow Wedding Films – Business Card</title>
<link rel="stylesheet" href="https://fonts.googleapis.com/css2?family=Josefin+Sans:wght@600&family=Lato:wght@400;900&display=swap">
<style>
  :root {
    --backdrop: #d9d9d7;
    --card-dark: #262626;
    --card-light: #f7f7f5;
    --gold: #c19a35;
    --gold-deep: #9c7721;
    --gold-light: #e6c65e;
    --ink: #141414;
  }
  * { margin: 0; padding: 0; box-sizing: border-box; }
  html, body { width: 900px; height: 1200px; overflow: hidden; }
  body {
    background: var(--backdrop);
    display: flex;
    flex-direction: column;
    align-items: center;
    justify-content: center;
    gap: 90px;
  }
  .card {
    position: relative;
    width: 740px;
    height: 423px;
    border-radius: 30px;
    overflow: hidden;
  }
  .card--front {
    background: var(--card-dark);
    display: flex;
    flex-direction: column;
    align-items: center;
    justify-content: center;
    font-family: "Josefin Sans", sans-serif;
    font-weight: 600;
    color: var(--gold);
    text-transform: uppercase;
  }
  .brand-name {
    font-size: 54px;
    letter-spacing: 0.22em;
    padding-left: 0.22em;
    line-height: 1;
  }
  .brand-tagline {
    margin-top: 18px;
    font-size: 25px;
    letter-spacing: 0.42em;
    padding-left: 0.42em;
    line-height: 1;
  }
  .card--back {
    background: var(--card-light);
    font-family: "Lato", sans-serif;
    color: var(--ink);
  }
  .gold-band {
    position: absolute;
    top: 0;
    right: 0;
    width: 200px;
    height: 100%;
    background: linear-gradient(160deg, var(--gold-light), var(--gold) 45%, var(--gold-deep));
  }
  .contact-block {
    position: absolute;
    left: 50px;
    top: 58px;
  }
  .contact-title {
    font-weight: 900;
    font-size: 20px;
    text-transform: uppercase;
    letter-spacing: -0.01em;
  }
  .divider {
    width: 22px;
    height: 4px;
    background: var(--gold);
    margin: 22px 0 16px;
  }
  .contact-list { list-style: none; }
  .contact-list li {
    display: flex;
    align-items: center;
    gap: 14px;
    font-size: 20px;
    line-height: 1;
    height: 32px;
  }
  .contact-icon {
    width: 20px;
    height: 20px;
    flex: none;
    fill: var(--ink);
  }
  .social-square {
    width: 20px;
    height: 20px;
    flex: none;
    background: var(--ink);
    border-radius: 3px;
  }
</style>
</head>
<body>
  <section class="card card--front" aria-label="Business card front">
    <div class="brand-name">Lewis Marrow</div>
    <div class="brand-tagline">Wedding Films</div>
  </section>

  <section class="card card--back" aria-label="Business card back">
    <div class="contact-block">
      <h1 class="contact-title">Lewis Marrow Wedding Films</h1>
      <div class="divider"></div>
      <ul class="contact-list">
        <li>
          <svg class="contact-icon" viewBox="0 0 24 24" aria-hidden="true"><path d="M6.6 10.8a15.1 15.1 0 0 0 6.6 6.6l2.2-2.2a1 1 0 0 1 1-.25 11.4 11.4 0 0 0 3.6.57 1 1 0 0 1 1 1V20a1 1 0 0 1-1 1A17 17 0 0 1 3 4a1 1 0 0 1 1-1h3.5a1 1 0 0 1 1 1c0 1.25.2 2.45.57 3.57a1 1 0 0 1-.25 1z"/></svg>
          07312 605 227
        </li>
        <li>
          <svg class="contact-icon" viewBox="0 0 24 24" aria-hidden="true"><path d="M2 5h20v14H2z M3.5 6.5 12 12.5l8.5-6" fill="none" stroke="#141414" stroke-width="0"/><path d="M2 5h20L12 12z"/><path d="M2 7l10 7 10-7v12H2z"/></svg>
          films@lewismarrowreels.com
        </li>
        <li>
          <svg class="contact-icon" viewBox="0 0 24 24" aria-hidden="true"><circle cx="12" cy="12" r="10"/><g fill="none" stroke="#f7f7f5" stroke-width="1.4"><ellipse cx="12" cy="12" rx="4.5" ry="10"/><path d="M2 12h20M4 7h16M4 17h16"/></g></svg>
          www.lewismarrowreels.com
        </li>
      </ul>
      <div class="divider"></div>
      <ul class="contact-list">
        <li><span class="social-square" aria-hidden="true"></span>@lewismarrowweddingfilms</li>
        <li><span class="social-square" aria-hidden="true"></span>@lewismarrowfilms</li>
      </ul>
    </div>
    <div class="gold-band" aria-hidden="true"></div>
  </section>
</body>
</html>
```